Large multi-office optometry business opening a Dry Eye Spa and needs sign.

Business name/sign info: Brenwick Dry Eye Institute, (555) 362-4817
Backlit pole sign at office entrance on a very busy street
Sign dimensions: 53" tall x 136.5" wide
State of the art Dry Eye Spa for treatment of all forms of dry eye and ocular surface disease. Also, have aesthetics treatments (IPL, Low Level Light Treatment, etc.)

Target Market(s)

People who are suffering from: dryness, burning, foreign body sensation, itching, fluctuating vision, tired eyes, etc.

Industry/Entity Type

Optometry and aesthetics

Colors
0054AA
0677BA
7BADD7
CADEEF
E8F1F8

Requirements
Must have
• Business name, phone number, subliminal message of relief in a glance or short look.
Nice to have
• Cool, relief, soothing sense.
Should not have
• Too much information or too busy.

```html
<!DOCTYPE html>
<html lang="en">
<head>
<meta charset="utf-8">
<title>Brenwick Dry Eye Institute – Pole Sign</title>
<link rel="stylesheet" href="https://fonts.googleapis.com/css2?family=Anton&family=Bebas+Neue&family=Montserrat:wght@500;600;700&display=swap">
<style>
  :root {
    --backdrop: #e6e8eb;
    --navy: #232a69;
    --sky: #2f8fd0;
    --sky-soft: #7badd7;
    --mist: #e8f1f8;
    --white: #ffffff;
    --grey-text: #555659;
    --rule: #2b5a8e;
  }
  html, body {
    margin: 0;
    padding: 0;
    width: 1200px;
    height: 556px;
    overflow: hidden;
    background: var(--backdrop);
  }
  .sign {
    position: absolute;
    left: 30px;
    top: 57px;
    width: 1140px;
    height: 441px;
    background: var(--white);
    box-shadow: 0 4px 18px rgba(0,0,0,0.12);
    overflow: hidden;
  }
  .sign svg { display: block; }
  .sign__place { font-family: "Bebas Neue", "Anton", sans-serif; fill: var(--sky); }
  .sign__name { font-family: "Anton", "Bebas Neue", sans-serif; fill: var(--white); }
  .sign__phone { font-family: "Montserrat", sans-serif; font-weight: 700; fill: var(--white); }
  .sign__services { font-family: "Montserrat", sans-serif; font-weight: 500; fill: var(--grey-text); }
  .sign__emblem {
    position: absolute;
    left: 861px;
    top: 33px;
    width: 244px;
    height: 353px;
    border-radius: 24px;
    background: linear-gradient(180deg, var(--sky-soft) 0%, var(--sky) 100%);
  }
</style>
</head>
<body>
  <div class="sign">
    <svg width="1140" height="441" viewBox="0 0 1140 441" xmlns="http://www.w3.org/2000/svg">
      <defs>
        <radialGradient id="groundShadow" cx="50%" cy="50%" r="50%">
          <stop offset="0" stop-color="#000" stop-opacity="0.22"/>
          <stop offset="1" stop-color="#000" stop-opacity="0"/>
        </radialGradient>
      </defs>

      <!-- navy field with diagonal edge -->
      <polygon class="sign__field" points="0,0 1140,0 1140,3 957,307 0,307" fill="var(--navy)"/>
      <!-- sky stripe -->
      <rect class="sign__stripe" x="0" y="307" width="957" height="10" fill="var(--sky)"/>

      <!-- place line -->
      <line x1="120" y1="77" x2="239" y2="77" stroke="var(--rule)" stroke-width="2"/>
      <line x1="630" y1="77" x2="755" y2="77" stroke="var(--rule)" stroke-width="2"/>
      <text class="sign__place" x="264" y="112" font-size="100" textLength="341" lengthAdjust="spacingAndGlyphs">BRENWICK</text>

      <!-- business name -->
      <text class="sign__name" x="47" y="241" font-size="118" textLength="776" lengthAdjust="spacingAndGlyphs">DRY EYE INSTITUTE</text>

      <!-- phone pill -->
      <ellipse cx="433" cy="352" rx="260" ry="8" fill="url(#groundShadow)"/>
      <rect class="sign__pill" x="155" y="277" width="556" height="64" rx="32" fill="var(--sky)"/>
      <circle cx="186" cy="309" r="27" fill="var(--navy)"/>
      <g class="sign__phone-icon" transform="translate(173 296)" fill="var(--white)">
        <path d="M3 2 C1 4 0 7 1 10 C3 16 9 22 15 25 C18 26 21 25 23 23 L24 21 C24 20 24 19 23 18 L19 15 C18 14.5 17 14.5 16 15.5 L14.5 17 C11.5 15.5 9.5 13.5 8 10.5 L9.5 9 C10.5 8 10.5 7 10 6 L7 2 C6 1 5 1 4 1.5 Z"/>
        <path d="M15 4 A8 8 0 0 1 22 11" stroke="var(--white)" stroke-width="2" fill="none" stroke-linecap="round"/>
        <path d="M15 8 A4 4 0 0 1 18 11" stroke="var(--white)" stroke-width="2" fill="none" stroke-linecap="round"/>
      </g>
      <text class="sign__phone" x="228" y="326" font-size="47" textLength="457" lengthAdjust="spacingAndGlyphs">Call (555) 362-4817</text>

      <!-- services -->
      <text class="sign__services" x="111" y="400" font-size="35" textLength="646" lengthAdjust="spacingAndGlyphs">IPL, Low Level Light Treatment, etc.</text>

      <!-- emblem shadow -->
      <ellipse cx="983" cy="413" rx="112" ry="10" fill="url(#groundShadow)"/>
    </svg>
    <div class="sign__emblem" role="img" aria-label="Emblem area: blue water drop containing a stylised eye"></div>
  </div>
</body>
</html>
```